Plakat/Banner-Design für Schnaps
Zielgruppe
Aufgabe des Unternehmens ist der europaweite Vetrieb von Getränken. In diesem Projekt besteht die Zielgruppe aus niederländern zwischen 18-25 Jahren.
Aufgabenstellung
Das Plakat-Design soll ansprechend wirken und direkt ins Auge stechen.
Gerne kann dabei auch mit Farben gearbeitet werden oder die Flasche in einen Hintergrund mit eingefügt werden. Der Kreativität sind keine Grenzen gesetzt.
Die Flasche muss dabei aber immer die Hauptrolle spielen und sollte sehr gut erkennbar sein und im Vordergrund stehen.
Um die Flasche ins beste Licht zu rücken kann diese auch gerne retuschiert werden oder mit einem "Wetlook-effekt" überzogen werden.
Die Internetseite "www.falmoor-liqueur.com" so wie der Spruch "Geen 18, geen alcohol" sollten auch im Fußbereich mit aufs Plakat.
Desweiteren soll das Plakat auch als Facebookbanner verwendet werden können.
Das Plakat wird an Retailer geschickt und bei diesen in oder vor den Geschäften platziert.
Die Größe des Plakats soll A1 sein.
Bei Fragen stehen wir jederzeit zur Verfügung.

```html
<!DOCTYPE html>
<html lang="nl">
<head>
<meta charset="utf-8">
<title>Falmoor Liqueur – Poster</title>
<link rel="stylesheet" href="https://fonts.googleapis.com/css2?family=Anton&family=Rubik+Dirt&family=Arimo:wght@400;700&display=swap">
<style>
  :root {
    --magenta: #e5007d;
    --yellow: #f4e80f;
    --ink: #0d0d0d;
    --paper: #ffffff;
    --bottle-dark: #151515;
    --bottle-mid: #3a3a3a;
  }
  * { margin: 0; padding: 0; box-sizing: border-box; }
  html, body { width: 848px; height: 1200px; overflow: hidden; background: var(--magenta); }
  .poster {
    position: relative;
    width: 848px;
    height: 1200px;
    background: var(--magenta);
    overflow: hidden;
    font-family: "Arimo", Arial, sans-serif;
  }
  .poster__shapes { position: absolute; inset: 0; }
  .headline {
    position: absolute;
    left: 150px;
    top: 378px;
    font-family: "Rubik Dirt", "Arial Black", sans-serif;
    font-size: 66px;
    line-height: 1;
    color: var(--paper);
    letter-spacing: 1px;
  }
  .brand-mark__name {
    font-family: "Anton", Impact, sans-serif;
    font-size: 34px;
    letter-spacing: 1px;
    fill: var(--paper);
  }
  .bottles {
    position: absolute;
    left: 328px;
    top: 462px;
    width: 402px;
    height: 488px;
    border-radius: 30px 30px 10px 10px;
    background: linear-gradient(90deg, var(--bottle-dark), var(--bottle-mid) 50%, var(--bottle-dark));
  }
  .footer {
    position: absolute;
    right: 55px;
    top: 978px;
    text-align: right;
    color: var(--ink);
  }
  .footer__url {
    font-family: "Anton", Impact, sans-serif;
    font-size: 37px;
    line-height: 1.05;
    text-transform: uppercase;
    letter-spacing: 0.5px;
  }
  .footer__claim {
    font-weight: 700;
    font-size: 19px;
    margin-top: 4px;
  }
  .footer__address {
    font-size: 8px;
    line-height: 1.35;
    margin-top: 6px;
  }
</style>
</head>
<body>
<main class="poster">
  <svg class="poster__shapes" width="848" height="1200" viewBox="0 0 848 1200" aria-hidden="true">
    <polygon class="floor" points="277,902 848,902 848,1200 453,1200" fill="var(--yellow)"/>
    <g class="diagonal-band">
      <line x1="-10" y1="360" x2="606" y2="-10" stroke="var(--ink)" stroke-width="26"/>
      <line x1="-10" y1="360" x2="606" y2="-10" stroke="var(--paper)" stroke-width="4"/>
    </g>
    <g class="frame" fill="none" stroke="var(--ink)" stroke-width="13">
      <rect x="40" y="38" width="774" height="1132"/>
    </g>
    <g class="brand-mark">
      <circle cx="260" cy="176" r="92" fill="var(--magenta)" stroke="var(--ink)" stroke-width="12"/>
      <text class="brand-mark__name" x="260" y="189" text-anchor="middle">FALMOOR</text>
    </g>
  </svg>

  <h1 class="headline">Hmmh ...</h1>

  <div class="bottles" role="img" aria-label="Three dark bottles of Falmoor Original liqueur standing side by side"></div>

  <footer class="footer">
    <p class="footer__url">www.falmoor-liqueur.com</p>
    <p class="footer__claim">Geen 18, geen alcohol</p>
    <p class="footer__address">Marten Vos Promo TRDrinkhaus GmbH<br>Kanalstraße 21<br>28321 Falmstedt<br>Deutschland</p>
  </footer>
</main>
</body>
</html>
```